Downloadable PDF "Brochure?"

We have a Free download we will provide in exchange for an email address on our new Trailmark website. The website at www.venturetrailmark-example.com is in development and will look nothing like what it currently does, but you can go there and get a sense of what Trailmark is from the text on the website. (see the attached image 'site design' for the new redesigned website for aesthetics).

We are looking for a nice design for the document, that will represent the mostly text document well. We are not actually looking to print these at a printer so they don't have to be print ready. I went ahead and included the logo and colors and fonts file again just for reference.

Target Market(s)

Business Owners / Decision Makers

Requirements
Must have
• See attached document 'trailmark freebie' for text to be utilized in the finished deliverable.
• See the attached image 'Site Design' for the website aesthetic.

```html
<!DOCTYPE html>
<html lang="en">
<head>
<meta charset="utf-8">
<title>Trailmark – Technology Advisors Brochure</title>
<link rel="stylesheet" href="https://fonts.googleapis.com/css2?family=Cinzel:wght@400;500&family=Open+Sans:wght@400;600&display=swap">
<style>
  :root{
    --backdrop:#8b8b8b;
    --shadow:#606060;
    --slate:#34474c;
    --copper:#c87b4f;
    --paper:#ffffff;
    --ink:#3d3d3d;
    --heading:#33383a;
    --rule:#555;
  }
  *{margin:0;padding:0;box-sizing:border-box}
  html,body{width:880px;height:1200px;overflow:hidden}
  body{background:var(--backdrop);position:relative;font-family:"Open Sans",Arial,sans-serif;color:var(--ink)}
  .page-shadow{position:absolute;width:361.6px;height:467.2px;background:var(--shadow)}
  .page{position:absolute;width:361.6px;height:467.2px;background:var(--paper);overflow:hidden}
  .abs{position:absolute}
  .display{font-family:"Cinzel",Georgia,serif;font-weight:400}

  /* cover */
  .cover-photo{left:0;top:0;width:100%;height:433.6px;background:linear-gradient(180deg,#c9d2cf 0%,#d9d0b4 38%,#b7b09a 62%,#7b7668 100%)}
  .cover-band-copper{left:0;top:433.6px;width:100%;height:18.4px;background:var(--copper)}
  .cover-band-slate{left:0;top:452px;width:100%;height:15.2px;background:var(--slate)}
  .brand-name{font-family:"Open Sans",Arial,sans-serif;font-weight:600;font-size:15px;letter-spacing:2px;line-height:1;color:var(--slate);text-align:center}
  .cover-brand{left:218px;top:100px;width:136px}
  .cover-panel{left:144.8px;top:165.6px;width:216.8px;height:179.2px;background:var(--slate)}
  .cover-panel-edge{left:144.8px;top:165.6px;width:9.6px;height:179.2px;background:var(--copper)}
  .tab-copper{background:var(--copper)}
  .cover-title{right:16.8px;top:216px;text-align:right;color:#fff;font-size:15.5px;line-height:21px;letter-spacing:.6px}
  .cover-sub{right:16.8px;top:270px;text-align:right;color:#fff;font-size:8.2px;line-height:10.4px}
  .cover-url{left:0;width:100%;top:437.5px;text-align:center;color:#fff;font-size:8.6px;letter-spacing:1.4px}

  /* inner pages */
  .strip-copper{left:0;top:0;width:24.8px;height:100%;background:var(--copper)}
  .intro-panel{left:0;top:13.6px;width:293.6px;height:125.6px;background:var(--slate)}
  .intro-edge{left:293.6px;top:0;width:9.6px;height:139.2px;background:var(--copper)}
  .intro-title{left:21.6px;top:30px;color:#fff;font-size:14px;line-height:16.5px;letter-spacing:.5px}
  .intro-rule{left:21.6px;top:68.8px;width:83px;height:1px;background:#e6e6e6}
  .intro-text{left:21.6px;top:82px;width:262px;color:#fff;font-size:6.3px;line-height:7.9px}

  .question{position:absolute;width:306px}
  .question h2{font-family:"Cinzel",Georgia,serif;font-weight:500;font-size:7px;line-height:9px;color:var(--heading);letter-spacing:.3px}
  .question h2::after{content:"";display:block;width:64px;height:1px;background:var(--copper);margin:3px 0 7px}
  .question p{font-size:5.3px;line-height:7px;color:var(--ink)}

  .footer-rule{height:.8px;background:var(--rule)}
  .footer-url{font-size:7.4px;letter-spacing:.8px;color:var(--heading);white-space:nowrap}

  .top-band{left:25.6px;top:0;width:336px;height:16px;background:var(--slate)}
  .top-band-gap{left:28.8px;top:0;width:3.2px;height:16px;background:#fff}

  .contact-box{left:0;top:321.6px;width:204px;height:124px;background:var(--slate)}
  .contact-edge{left:204px;top:321.6px;width:12.8px;height:124px;background:var(--copper)}
  .contact-label{left:28px;top:337px;color:#fff;font-family:"Cinzel",Georgia,serif;font-size:7px;letter-spacing:.4px}
  .contact-row{position:absolute;left:30px;display:flex;align-items:flex-start;gap:6px;color:#fff;font-size:8.4px;line-height:10.8px;white-space:nowrap}
  .contact-row svg{flex:none;width:12px;height:12px;margin-top:-.5px}
  .back-brand{left:226px;top:390px;width:130px}
</style>
</head>
<body>

<div class="page-shadow" style="left:80px;top:132px"></div>
<div class="page-shadow" style="left:489.6px;top:132px"></div>
<div class="page-shadow" style="left:80px;top:656px;height:468px"></div>
<div class="page-shadow" style="left:489.6px;top:656px;height:468px"></div>

<!-- cover -->
<section class="page cover" style="left:57.6px;top:110.4px">
  <div class="abs cover-photo" role="img" aria-label="Photo of a businessman drawing back a tall curtain to reveal an open road under a bright sky"></div>
  <div class="abs brand-name cover-brand">TRAILMARK</div>
  <div class="abs tab-copper" style="left:320px;top:148px;width:41.6px;height:17.6px"></div>
  <div class="abs cover-panel"></div>
  <div class="abs cover-panel-edge"></div>
  <div class="abs tab-copper" style="left:320px;top:344.8px;width:41.6px;height:18.4px"></div>
  <h1 class="abs display cover-title">Technology Advisors<br>That "Get" Business</h1>
  <p class="abs cover-sub">We help you leverage technology to create<br>a competitive advantage</p>
  <div class="abs cover-band-copper"></div>
  <div class="abs cover-band-slate"></div>
  <div class="abs cover-url">www.venturetrailmark-example.com</div>
</section>

<!-- page 2 -->
<section class="page" style="left:467.2px;top:110.4px">
  <div class="abs strip-copper"></div>
  <div class="abs intro-edge"></div>
  <div class="abs intro-panel"></div>
  <h1 class="abs display intro-title">10 Questions To Choose<br>The Best Technology Advisor</h1>
  <div class="abs intro-rule"></div>
  <p class="abs intro-text">When you choose a technology advisor whether it be a Managed Service Provider, fractional CIO or a full-time CIO you need to make sure that they understand business just as much as they understand technology. Some of the biggest complaints about the IT department are that they just don't "Get it". The questions below should help you determine whether or not they have a technology mindset or a business mindset.</p>

  <div class="question" style="left:36.8px;top:149px">
    <h2>What is scalability? How important is it from a technology perspective on a scale of 1-&gt;10 with 10 being the highest? What all does scalability impact?</h2>
    <p>This question is designed to get a reading on the person's mindset. A typical technology-minded response would be something describing the ability of systems or software to scale by adding additional resources. When working from a business point of view, however, you want to see it defined as the ability for the organization to support increased volume without sacrificing margins. The importance of this concept cannot be overstated and should be a 9 or 10 in terms of ranking. Regarding impact, you want to see not just an understanding of having to spend money two or three times for a different solution to the same problem, but an acknowledgment of the 'total' cost, including adoption fatigue, the opportunity cost of change, and the competitive disadvantage it creates. For concepts of business scalability refer to 'Growing Tall' by Dale Pruett.</p>
  </div>

  <div class="question" style="left:36.8px;top:268px">
    <h2>Provide an example where you solved a problem without the use of technology.</h2>
    <p>Often technology-minded individuals become so wrapped up in the solutions themselves they fail to realize a policy or process change is far more effective and simple than making changes to existing or introducing new technology. Asking for a specific example here should demonstrate the ability to think from a business mindset. For specific examples reference 'The Ember Project' by Lane, Otis, and Vale.</p>
  </div>

  <div class="question" style="left:36.8px;top:346px">
    <h2>How do you go about prioritizing solutions in order of importance for implementation / adoption?</h2>
    <p>Answers here should include reference to some form of discovery process or a thorough evaluation at the operations level. One of the key skill sets for someone approaching technology from a business point of view is mapping solutions and their respective importance to business outcomes and (often more importantly) eliminating bottlenecks while respecting that some implementations must necessarily come before others to be viable. For reference on the Theory of Constraints see 'The Target' by Aaron Feldt.</p>
  </div>

  <div class="abs footer-rule" style="left:32px;top:443px;width:140px"></div>
  <div class="abs footer-url" style="right:17px;top:437.5px">www.venturetrailmark-example.com</div>
</section>

<!-- page 3 -->
<section class="page" style="left:57.6px;top:634.4px;height:468px">
  <div class="abs strip-copper" style="width:25.6px"></div>
  <div class="abs top-band"></div>
  <div class="abs top-band-gap"></div>

  <div class="question" style="left:36.8px;top:35px">
    <h2>What is Information Technology Debt?</h2>
    <p>Stated simply, 'IT Debt' is a measurement of the out-of-date, incomplete or yet-to-be-defined technology changes. Debt occurs for a number of reasons, including lack of qualified personnel to implement the needed solutions (or recognize the problem in the first place); historical spending haunting the organization "we spent money on something like this before and look what it got us"; Fire-fighting (addressing issues purely reactively in a downward spiral leaving no time for fixing the real underlying problem); or most commonly, the budget being already allocated to other company endeavors that seem immediately more pressing. By recognizing what IT Debt is, the individual demonstrates an acknowledgment of how impactful it can be when neglected and not brought to the forefront of business planning sessions.</p>
  </div>

  <div class="question" style="left:36.8px;top:133px">
    <h2>Provide an example where you argued against implementing a technology solution and why.</h2>
    <p>Despite it being seemingly obvious, using 'outside of budget' is not a good answer. Business-minded technology advisors should be intimately aware of how well a proposed solution will integrate into the existing company ecosystem (software tools already present, workflow, and processes), if it drives the company toward reducing/eliminating a bottleneck (and thereby creates more leverage), and if it fits the company's culture. If any of these are a no, the solution should be carefully examined for what it really offers the organization. If yes, the budget should be evaluated as a cost-benefit analysis, not a flat number 'not to exceed'.</p>
  </div>

  <div class="question" style="left:36.8px;top:230px">
    <h2>What is your ideal method for maintaining technology alignment for the company?</h2>
    <p>You want to see a specific process envisioned here. At the very least a recommendation to be involved in business planning meetings or retreats, and ideally a standing technology focused meeting with leadership present should be argued for. For technology to be truly in alignment, it must fit the needs of the organization, not the other way around. This needs to come from the top level, and it means a representative must be present in critical business strategy meetings to understand where the company is headed, what operational constraints they are encountering, and what their short-term goals are. For an outline of how this model has been the underlying key to success for several well-known companies reference 'Fine to Finest' by Ray Colton.</p>
  </div>

  <div class="question" style="left:36.8px;top:332px">
    <h2>How do you plan on measuring and monitoring the adoption success of a solution or project?</h2>
    <p>Technically minded individuals often look at the point of 'it's up and running and it all works', as where their responsibilities end. Someone with a business mindset should demonstrate that evaluating how well the solution has been adopted into the day to day workflow, and to what degree the solution has increased leverage or operational transparency are the true critical indicators of success. There should be a specific process of follow-up after implementation to flag adoption or workflow issues due to problems such as inadequate training, unforeseen incompatibilities (whether they be process or technology related), or simply resistance to change. These findings can then be brought back to leadership to evaluate how best to improve successful adoption going forward.</p>
  </div>

  <div class="abs footer-rule" style="left:32px;top:444.8px;width:140px"></div>
  <div class="abs footer-url" style="right:17px;top:439px">www.venturetrailmark-example.com</div>
</section>

<!-- page 4 -->
<section class="page" style="left:467.2px;top:634.4px;height:468px">
  <div class="abs strip-copper"></div>

  <div class="question" style="left:36.8px;top:30px">
    <h2>Provide an example where you had to balance customer and employee technology experience with security and compliance.</h2>
    <p>A critical role fulfilled by a technology advisor is being able to balance maintaining compliance and sound security practices with as painless of a technology experience as possible. They should be able to weigh the critical importance of protecting the organization from the negative public relations and liability of a security flaw while respecting that a solution must not be unusable to be useful. Look for an example that demonstrates an understanding of both sides and strikes a balance without going to an extreme in either direction.</p>
  </div>

  <div class="question" style="left:36.8px;top:121px">
    <h2>What would you do first, if you were selected as our advisor? Can you give me details on what your discovery or on-boarding process includes?</h2>
    <p>You are looking to make sure that they don't stop at the technology. There should be a higher focus on understanding what the company processes are and how the people inside the organization get work done. If they focus only on network, security, and disaster recovery assessments then they do not have a business mindset.</p>
  </div>

  <div class="question" style="left:36.8px;top:206px">
    <h2>Can you give me an example of a time you gave a suggestion for a solution and it was not taken? Describe the solution and why it was important to the organization. And why do you think they didn't implement it?</h2>
    <p>When they describe why they think the solution was important do they simply talk about risk reduction or uptime improvements without tying them back to an organizational goal or bottleneck. Being able to demonstrate actual business value is a critical skill for a technology advisor. For reference on technical excellence in service of business objectives rather than blindly servicing requirements see 'A Chair at the Desk' by Neil Sorensen.</p>
  </div>

  <div class="abs contact-box"></div>
  <div class="abs contact-edge"></div>
  <div class="abs contact-label">CONTACT US</div>

  <div class="contact-row" style="top:358px">
    <svg viewBox="0 0 12 12" aria-hidden="true"><circle cx="6" cy="6" r="6" fill="#c87b4f"/><rect x="4" y="2.6" width="4" height="6.8" rx=".8" fill="none" stroke="#fff" stroke-width=".9"/></svg>
    <span>(555) 010-0580</span>
  </div>
  <div class="contact-row" style="top:376px">
    <svg viewBox="0 0 12 12" aria-hidden="true"><circle cx="6" cy="6" r="6" fill="#c87b4f"/><rect x="3" y="3.8" width="6" height="4.4" fill="none" stroke="#fff" stroke-width=".8"/><path d="M3 3.8 6 6.3 9 3.8" fill="none" stroke="#fff" stroke-width=".8"/></svg>
    <span style="font-size:7.2px">jmarlow@venturetrailmark-example.com</span>
  </div>
  <div class="contact-row" style="top:394px">
    <svg viewBox="0 0 12 12" aria-hidden="true"><circle cx="6" cy="6" r="6" fill="#c87b4f"/><circle cx="6" cy="6" r="3.3" fill="none" stroke="#fff" stroke-width=".8"/><path d="M2.7 6h6.6M6 2.7c-1.6 2-1.6 4.6 0 6.6M6 2.7c1.6 2 1.6 4.6 0 6.6" fill="none" stroke="#fff" stroke-width=".7"/></svg>
    <span style="font-size:7.6px">www.venturetrailmark-example.com</span>
  </div>
  <div class="contact-row" style="top:412px">
    <svg viewBox="0 0 12 12" aria-hidden="true"><path d="M6 0.5a4.3 4.3 0 0 1 4.3 4.3C10.3 8 6 11.8 6 11.8S1.7 8 1.7 4.8A4.3 4.3 0 0 1 6 .5z" fill="#c87b4f"/><circle cx="6" cy="4.8" r="1.5" fill="#fff"/></svg>
    <span>1200 Ridgeway Parkway<br>Suite 200, Lakeview, TX 77000</span>
  </div>

  <div class="abs brand-name back-brand">TRAILMARK</div>
</section>

</body>
</html>
```